Design a sleek website for a Global parking app

We need a sleek website for a soon-to-be-launched global parking app called 'Vantly'.

Please see attached specs for the site's three example pages for which we need designs. I have also included:
- Original, high-res versions of the images contained in the Word docs
- Vantly business card
- Vantly logos

Industry/Entity Type

Parking

Coding

Coded - Design and coding required

Number of Pages Required

3 page

Colors
1b1b1b
ffffff

Requirements
Must have
• - Sleek design, which ties in with the brand
• - Complete look and feel for the three key pages spec'd out

```html
<!DOCTYPE html>
<html lang="en">
<head>
<meta charset="utf-8">
<title>Vantly – Your private parking space</title>
<link href="https://fonts.googleapis.com/css2?family=Roboto:wght@300;400;500;700&display=swap" rel="stylesheet">
<style>
:root{
  --ink:#1b1b1b;
  --white:#ffffff;
  --accent:#ef5a5f;
  --accent-soft:#f08a8c;
  --text:#3d3d3d;
  --muted:#777;
  --footer:#3b3b3b;
  --footer-base:#262626;
  --line:#cfcfcf;
}
*{box-sizing:border-box;margin:0;padding:0}
html,body{width:1200px;height:4196px;overflow:hidden}
body{position:relative;background:var(--white);font-family:"Roboto",Arial,sans-serif;color:var(--text)}
.abs{position:absolute}
.btn{position:absolute;background:var(--accent);color:var(--white);font-size:13px;font-weight:500;letter-spacing:.5px;display:flex;align-items:center;justify-content:center;border-radius:2px;text-transform:uppercase}
.photo{position:absolute}

/* hero */
.hero{position:absolute;left:0;top:0;width:1200px;height:694px;background:linear-gradient(160deg,#5a5a5a 0%,#2c2c2c 45%,#4a4a4a 75%,#1e1e1e 100%)}
.top-nav{position:absolute;top:40px;right:92px;display:flex;gap:26px;font-size:13px;font-weight:500;color:var(--white);letter-spacing:.4px}
.top-nav span{display:flex;align-items:center;gap:6px}
.top-nav i{width:10px;height:10px;border-radius:50%;background:var(--white);display:inline-block}
.slider-arrow{position:absolute;top:345px;color:#ddd;font-size:22px}
.brand-mark{position:absolute;left:540px;top:154px;width:120px;height:120px;background:var(--white);border-radius:8px}
.brand-name{position:absolute;left:0;width:1200px;top:292px;text-align:center;color:var(--white);font-size:26px;font-weight:400;letter-spacing:9px}
.tagline{position:absolute;left:0;width:1200px;top:332px;text-align:center;color:var(--white);font-size:15px}
.hero .btn{left:495px;top:378px;width:207px;height:44px;font-size:19px;border:2px solid #f7a7a9;border-radius:3px}
.vehicle-icons{position:absolute;left:426px;top:456px;display:flex;gap:17px}
.vehicle-icons svg{width:72px;height:72px}
.search-strip{position:absolute;left:0;top:573px;width:1200px;height:121px;background:rgba(20,20,20,.72)}
.field-label{position:absolute;top:25px;font-size:12px;font-weight:500;color:var(--white);text-transform:uppercase}
.field{position:absolute;top:54px;height:41px;background:var(--white);border-radius:2px;font-size:12px;color:#888;padding:0 12px;display:flex;align-items:center;justify-content:space-between}
.search-strip .btn{left:965px;top:54px;width:120px;height:41px;font-size:12px}

/* features */
.feature h2{position:absolute;font-size:29px;font-weight:400;color:var(--ink);line-height:1.3}
.feature p{position:absolute;font-size:12.5px;line-height:1.6;color:var(--muted)}

/* explore */
.section-title{position:absolute;left:0;width:1200px;text-align:center;color:var(--ink);font-weight:400;text-transform:uppercase;letter-spacing:1px}
.city{position:absolute;width:319px;height:277px}
.city span{position:absolute;left:0;bottom:0;width:100%;height:32px;background:rgba(30,30,30,.7);color:var(--white);font-size:13px;font-weight:500;display:flex;align-items:center;justify-content:center;text-transform:uppercase}

/* day band */
.day-band{position:absolute;left:0;top:2246px;width:1200px;height:445px;background:linear-gradient(180deg,#3a4350 0%,#4b5560 50%,#2f3a33 100%)}
.day-band .mark{position:absolute;left:550px;top:115px;width:100px;height:100px;background:var(--white);border-radius:6px}
.day-band h2{position:absolute;left:0;width:1200px;top:240px;text-align:center;color:var(--white);font-size:47px;font-weight:500;letter-spacing:1px}
.day-band p{position:absolute;left:0;width:1200px;top:306px;text-align:center;color:var(--white);font-size:18px}

/* community */
.member{position:absolute;top:2867px;width:241px;height:275px}
.member-name{position:absolute;top:3160px;width:241px;text-align:center;font-size:18px;color:#555;text-transform:uppercase;letter-spacing:.5px}
.featured{position:absolute;left:106px;top:2867px;width:244px;height:364px;border:3px solid #f5c4c6;background:var(--white)}
.featured .panel{position:absolute;left:11px;top:11px;width:216px;height:246px;background:var(--accent-soft);color:var(--white);text-align:center}
.featured .panel h3{margin-top:52px;font-size:24px;font-weight:400;letter-spacing:1px}
.featured .panel p{margin:12px 20px 0;font-size:11.5px;line-height:1.55}
.featured .who{position:absolute;left:0;width:238px;top:280px;text-align:center;font-size:16px;color:#555}
.dots{position:absolute;display:flex;gap:6px}
.dots i{width:20px;height:20px;border:1.5px solid #999;border-radius:50%;display:block}

/* alerts */
.alerts{position:absolute;left:0;top:3300px;width:1200px;height:509px;background:linear-gradient(100deg,#2b2b2b 0%,#4e4944 45%,#2a2a2a 100%)}
.alerts h2{position:absolute;left:0;width:1200px;top:104px;text-align:center;color:var(--white);font-size:30px;font-weight:500;line-height:1.4;text-transform:uppercase}
.input{position:absolute;height:37px;border:1.5px solid #ddd;color:var(--white);font-size:12px;padding:10px 12px}
.alerts .btn{left:453px;top:384px;width:274px;height:36px;font-size:14px}

/* footer */
.footer{position:absolute;left:0;top:3809px;width:1200px;height:289px;background:var(--footer)}
.lang{position:absolute;left:126px;top:42px;width:232px;height:39px;border:1.5px solid #bbb;color:var(--white);font-size:12px;padding:12px 14px}
.lang b{position:absolute;right:14px;top:10px;font-weight:400}
.footer .mark{position:absolute;left:126px;top:107px;width:92px;height:92px;background:#9a9a9a}
.footer .brand{position:absolute;left:126px;top:218px;width:92px;text-align:center;color:#bbb;font-size:18px;letter-spacing:6px}
.foot-col{position:absolute;top:46px;color:#ddd;font-size:13px;line-height:24px}
.foot-col h4{font-size:14px;font-weight:500;color:var(--white);margin-bottom:4px;text-transform:uppercase}
.foot-base{position:absolute;left:0;top:4098px;width:1200px;height:98px;background:var(--footer-base)}
.foot-base p{position:absolute;left:0;width:1200px;top:22px;text-align:center;font-size:11px;color:#aaa}
.foot-base .dots{left:546px;top:50px}
.foot-base .dots i{border-color:#ccc}
</style>
</head>
<body>

<header class="hero">
  <div class="photo" role="img" aria-label="Aerial black and white view of city skyscrapers" style="inset:0;background:linear-gradient(150deg,rgba(255,255,255,.08),rgba(0,0,0,.25))"></div>
  <nav class="top-nav">
    <span>LEASE YOUR PARKING SPACE FOR FREE</span>
    <span><i></i>LOG IN</span>
    <span><i></i>SIGN UP</span>
    <span><i></i>HELP</span>
  </nav>
  <span class="slider-arrow" style="left:38px">‹</span>
  <span class="slider-arrow" style="right:38px">›</span>
  <div class="brand-mark"></div>
  <div class="brand-name">VANTLY™</div>
  <div class="tagline">Your private parking space</div>
  <div class="btn">How it works</div>
  <div class="vehicle-icons">
    <svg viewBox="0 0 72 72" aria-label="Car"><circle cx="36" cy="36" r="33" fill="none" stroke="#fff" stroke-width="3"/><path d="M18 42h36v-7l-5-2-5-7H28l-5 7-5 2z" fill="#fff"/><circle cx="26" cy="44" r="4" fill="#fff"/><circle cx="46" cy="44" r="4" fill="#fff"/></svg>
    <svg viewBox="0 0 72 72" aria-label="Boat"><circle cx="36" cy="36" r="33" fill="none" stroke="#fff" stroke-width="3"/><path d="M37 16v24h14zM34 20L22 40h12zM18 44h36l-5 8H23z" fill="#fff"/></svg>
    <svg viewBox="0 0 72 72" aria-label="Scooter"><circle cx="36" cy="36" r="33" fill="none" stroke="#fff" stroke-width="3"/><path d="M20 44c2-8 10-10 18-8l8-12h5l-7 14 6 6z" fill="#fff"/><circle cx="24" cy="46" r="5" fill="#fff"/><circle cx="50" cy="46" r="5" fill="#fff"/></svg>
    <svg viewBox="0 0 72 72" aria-label="Helicopter"><circle cx="36" cy="36" r="33" fill="none" stroke="#fff" stroke-width="3"/><path d="M18 22h36v2H18zM35 24h2v5h-2zM26 30h18a6 6 0 010 12H30zM14 33h14v3H14zM28 46h18v2H28z" fill="#fff"/></svg>
  </div>
  <form class="search-strip">
    <span class="field-label" style="left:98px">Where do you want to park?</span>
    <span class="field-label" style="left:333px">Check in</span>
    <span class="field-label" style="left:540px">Check out</span>
    <span class="field-label" style="left:744px">Vehicle type</span>
    <div class="field" style="left:98px;width:224px"></div>
    <div class="field" style="left:333px;width:195px">dd - mm - yyyy <span>▦</span></div>
    <div class="field" style="left:540px;width:193px">dd - mm - yyyy <span>▦</span></div>
    <div class="field" style="left:744px;width:199px"></div>
    <div class="btn">Search now</div>
  </form>
</header>

<section class="feature">
  <div class="photo" role="img" aria-label="Blue scooter parked against a stone wall" style="left:98px;top:755px;width:500px;height:308px;background:linear-gradient(120deg,#c9b190 0%,#9f8566 40%,#2d6fae 60%,#6a5a48 100%)"></div>
  <h2 style="left:638px;top:775px">Parking Your Vehicle<br>Just Got Easier</h2>
  <p style="left:638px;top:872px;width:462px">Finding a place to park no longer means circling the block. Browse private spaces near where you are going, compare prices, book in seconds and pull straight in. Every space is listed by a local owner who knows the street, so you arrive calm and on time for what matters.</p>
  <div class="btn" style="left:638px;top:1004px;width:218px;height:39px">Click here for view info</div>
</section>

<section class="feature">
  <h2 style="left:98px;top:1113px">Leasing your private<br>parking space</h2>
  <p style="left:98px;top:1208px;width:460px">Leasing your private parking space just made extra cash easy, sharing your idle space with drivers who need it most.<br>List your driveway, garage or bay in minutes, set the hours that suit you and get paid for every booking. You stay in control of who parks and when.</p>
  <div class="btn" style="left:98px;top:1345px;width:218px;height:39px">Click here for view info</div>
  <div class="photo" role="img" aria-label="Close up of a classic car wheel beside a wooden boardwalk" style="left:598px;top:1099px;width:501px;height:305px;background:linear-gradient(100deg,#d9d9d9 0%,#a9a9a9 45%,#5c5e63 75%,#2f3034 100%)"></div>
</section>

<section class="explore">
  <h2 class="section-title" style="top:1480px;font-size:30px;line-height:1.3">Explore the world of Vantly.<br>See where other people are parking.</h2>
  <div class="city" role="img" aria-label="Sydney street detail" style="left:98px;top:1583px;background:linear-gradient(135deg,#4a4a4a,#2a2a2a 60%,#6a6a6a)"><span>Sydney</span></div>
  <div class="city" role="img" aria-label="Adelaide vineyard post with vines" style="left:439px;top:1583px;background:linear-gradient(180deg,#3d86c8 0%,#5f9e3b 55%,#6f5f46 100%)"><span>Adelaide</span></div>
  <div class="city" role="img" aria-label="Melbourne scooter against a graffiti wall" style="left:780px;top:1583px;background:linear-gradient(135deg,#c8415a,#d8a13a 40%,#3b5fa8 75%,#e5e5e5)"><span>Melbourne</span></div>
  <div class="city" role="img" aria-label="Paris river with boats and tower" style="left:98px;top:1882px;background:linear-gradient(180deg,#c9d3dc 0%,#8b949a 50%,#3a4a50 100%)"><span>Paris</span></div>
  <div class="city" role="img" aria-label="Barcelona balconies and flags" style="left:439px;top:1882px;background:linear-gradient(160deg,#3a3024,#b07a4a 45%,#d6a463 70%,#2a2520)"><span>Barcelona</span></div>
  <div class="city" role="img" aria-label="San Francisco Victorian house" style="left:780px;top:1882px;background:linear-gradient(180deg,#d8dde2 0%,#7a7f86 50%,#4a4d52 100%)"><span>San Francisco</span></div>
</section>

<section class="day-band" role="img" aria-label="City skyline across a river at dusk with flowers in the foreground">
  <div class="mark"></div>
  <h2>JUST FOR THE DAY</h2>
  <p>Discover private parking spots in your city</p>
</section>

<section class="community">
  <h2 class="section-title" style="top:2748px;font-size:40px">Our Community</h2>
  <p class="abs" style="left:0;width:1200px;top:2800px;text-align:center;font-size:13px;color:var(--muted)">of Parking Owners &amp; Renters</p>
  <div class="featured">
    <div class="panel">
      <h3>MAYA</h3>
      <p>Maya rents out her spare bay near the station, and drivers get an easy, affordable spot each day.</p>
    </div>
    <div class="who">MAYA</div>
    <div class="dots" style="left:71px;top:318px"><i></i><i></i><i></i><i></i></div>
  </div>
  <div class="member" role="img" aria-label="Portrait of community member Simon" style="left:355px;background:linear-gradient(160deg,#e4e4e4,#7a5a48 55%,#3a2a22)"></div>
  <div class="member" role="img" aria-label="Portrait of community member Barbara in a car" style="left:604px;background:linear-gradient(160deg,#2a2a2a,#a0705a 50%,#b23a32)"></div>
  <div class="member" role="img" aria-label="Portrait of community member Hasif" style="left:853px;background:linear-gradient(160deg,#d9d9d9,#8c6a58 55%,#5a4a44)"></div>
  <div class="member-name" style="left:355px">Simon</div>
  <div class="member-name" style="left:604px">Barbara</div>
  <div class="member-name" style="left:853px">Hasif</div>
</section>

<section class="alerts" role="img" aria-label="Smiling woman at the wheel of a car, darkened">
  <h2>Find your private parking space<br>through Vantly alerts</h2>
  <div class="input" style="left:282px;top:213px;width:308px">First Name :</div>
  <div class="input" style="left:610px;top:213px;width:305px">Last Name :</div>
  <div class="input" style="left:282px;top:263px;width:308px">Email :</div>
  <div class="input" style="left:610px;top:263px;width:305px;height:90px">Where do you need to park?</div>
  <div class="input" style="left:282px;top:316px;width:308px">Mobile :</div>
  <div class="btn">Sign up</div>
</section>

<footer class="footer">
  <div class="lang">English<b>⌄</b></div>
  <div class="mark"></div>
  <div class="brand">VANTLY</div>
  <div class="foot-col" style="left:475px">
    <h4>Vantly™</h4>
    About<br>Vantly Services<br>Press<br>Work for Vantly<br>Help<br>Policies<br>Terms &amp; Privacy<br>Contact Us
  </div>
  <div class="foot-col" style="left:699px">
    <h4>Discover</h4>
    Trust and Safety<br>Invite Friends<br>Parking Alerts<br>Vantly Picks<br>Mobile<br>Site Map
  </div>
  <div class="foot-col" style="left:929px">
    <h4>Leasing</h4>
    Lease your space for FREE<br>Responsible leasing<br>Vantly Community<br>Safe Parking
  </div>
</footer>
<div class="foot-base">
  <p>©2015 - 2016 <b>VANTLY TECHNOLOGIES PTY. LTD.</b>, All Rights Reserved.</p>
  <div class="dots"><i></i><i></i><i></i><i></i></div>
</div>

</body>
</html>
```